Quillfenner Tashby & Associates

Simple business cards for consulting firm specializing in non profit program design, evaluation and resource development,

Industry/Entity Type

Business

```html
<!DOCTYPE html>
<html lang="en">
<head>
<meta charset="utf-8">
<title>Quillfenner Tashby &amp; Associates – Business Card</title>
<link rel="stylesheet" href="https://fonts.googleapis.com/css2?family=Montserrat:wght@300;400;500;600&display=swap">
<style>
  :root {
    --stage: #2b2b2b;
    --card-black: #000000;
    --band-top: #6a6a6a;
    --band-bottom: #3e3e3e;
    --accent: #f2ea1c;
    --ink-light: #ffffff;
    --ink-soft: #e6e6e6;
  }
  html, body {
    margin: 0;
    padding: 0;
    width: 1200px;
    height: 900px;
    overflow: hidden;
    background: var(--stage);
    font-family: "Montserrat", sans-serif;
  }
  .canvas {
    position: relative;
    width: 1200px;
    height: 900px;
  }
  .business-card {
    position: absolute;
    left: 100px;
    top: 160px;
    width: 1000px;
    height: 580px;
    background: var(--card-black);
    overflow: hidden;
    box-shadow: 0 18px 40px rgba(0,0,0,0.45);
  }
  .contact-band {
    position: absolute;
    left: 0;
    top: 330px;
    width: 100%;
    height: 250px;
    background: linear-gradient(180deg, var(--band-top) 0%, var(--band-bottom) 100%);
  }
  .brand-mark {
    position: absolute;
    left: 50%;
    top: 38px;
    width: 84px;
    height: 84px;
    margin-left: -42px;
    box-sizing: border-box;
    border: 6px solid var(--accent);
    border-radius: 50%;
  }
  .firm-name {
    position: absolute;
    left: 0;
    top: 146px;
    width: 100%;
    margin: 0;
    text-align: center;
    font-weight: 400;
    font-size: 38px;
    line-height: 46px;
    letter-spacing: 1px;
    text-transform: uppercase;
  }
  .firm-name-first {
    display: block;
    color: var(--ink-light);
  }
  .firm-name-second {
    display: block;
    color: var(--accent);
  }
  .firm-tagline {
    position: absolute;
    left: 0;
    top: 252px;
    width: 100%;
    margin: 0;
    text-align: center;
    color: var(--ink-soft);
    font-weight: 300;
    font-size: 22px;
    letter-spacing: 0.5px;
  }
  .person {
    position: absolute;
    left: 130px;
    top: 420px;
    color: var(--ink-light);
  }
  .person-name {
    margin: 0;
    font-weight: 500;
    font-size: 34px;
    line-height: 40px;
  }
  .person-role {
    margin: 4px 0 0;
    font-weight: 300;
    font-size: 21px;
    color: var(--ink-soft);
  }
  .person-phone {
    display: flex;
    align-items: center;
    gap: 14px;
    margin-top: 26px;
    font-weight: 300;
    font-size: 22px;
  }
  .contact-list {
    position: absolute;
    left: 580px;
    top: 352px;
    margin: 0;
    padding: 0;
    list-style: none;
    color: var(--ink-light);
    font-weight: 300;
    font-size: 20px;
    line-height: 26px;
  }
  .contact-item {
    display: flex;
    align-items: flex-start;
    gap: 14px;
    margin-bottom: 8px;
  }
  .contact-icon {
    flex: none;
    width: 20px;
    height: 20px;
    margin-top: 3px;
  }
  .contact-icon path, .contact-icon circle, .contact-icon rect {
    fill: none;
    stroke: var(--accent);
    stroke-width: 1.8;
    stroke-linecap: round;
    stroke-linejoin: round;
  }
</style>
</head>
<body>
<div class="canvas">
  <section class="business-card">
    <div class="brand-mark" aria-hidden="true"></div>
    <h1 class="firm-name">
      <span class="firm-name-first">Quillfenner</span>
      <span class="firm-name-second">Tashby &amp; Associates</span>
    </h1>
    <p class="firm-tagline">Nonprofit Program Design &amp; Evaluation</p>

    <div class="contact-band"></div>

    <div class="person">
      <h2 class="person-name">Marlo Vence</h2>
      <p class="person-role">Consultant</p>
      <div class="person-phone">
        <svg class="contact-icon" viewBox="0 0 20 20" aria-hidden="true">
          <path d="M5 2.5 L7.5 2.5 L9 6.5 L7 8 C8 10.5 9.5 12 12 13 L13.5 11 L17.5 12.5 L17.5 15 C17.5 16.5 16 17.5 14.5 17.5 C8 17 3 12 2.5 5.5 C2.5 4 3.5 2.5 5 2.5 Z"/>
        </svg>
        <span>555.014.2260</span>
      </div>
    </div>

    <ul class="contact-list">
      <li class="contact-item">
        <svg class="contact-icon" viewBox="0 0 20 20" aria-hidden="true">
          <rect x="2" y="4.5" width="16" height="11" rx="1"/>
          <path d="M2.5 5 L10 11 L17.5 5"/>
        </svg>
        <span>hello@quillfenner.org</span>
      </li>
      <li class="contact-item">
        <svg class="contact-icon" viewBox="0 0 20 20" aria-hidden="true">
          <circle cx="10" cy="10" r="7.5"/>
          <path d="M2.5 10 H17.5 M10 2.5 C6.5 6.5 6.5 13.5 10 17.5 M10 2.5 C13.5 6.5 13.5 13.5 10 17.5"/>
        </svg>
        <span>www.quillfenner.org</span>
      </li>
      <li class="contact-item">
        <svg class="contact-icon" viewBox="0 0 20 20" aria-hidden="true">
          <path d="M10 18 C6 13 4 10 4 7.5 C4 4.2 6.7 2 10 2 C13.3 2 16 4.2 16 7.5 C16 10 14 13 10 18 Z"/>
          <circle cx="10" cy="7.5" r="2.2"/>
        </svg>
        <span>48 Larkmoor Lane<br>Fernvale - ST 00000</span>
      </li>
    </ul>
  </section>
</div>
</body>
</html>
```